One Page Website for Personal Trainer in London

I have a logo and need a one page website designed around my branding. I am a freelance Personal Trainer based in London specialising in bodyweight training for men and women. I would like the site to be modern and clean but not overtly urban in design.
I need the following headings:
About Me
My Services
Events
Blog
I don't need them to be seperate pages but if they can link to further down the page that would be great.
Industry/Entity Type
Personal Trainer
Coding
Coded - Design and coding required
Number of Pages Required
1 page
Requirements
Must have
- I need the following headings:
- About Me
- My Services
- Events
- Blog
- mobile friendly formatting
- health and fitness related photography
- Colour scheme in keeping with my existing logo

```html
<!DOCTYPE html>
<html lang="en">
<head>
<meta charset="utf-8">
<title>Marisa Holt – Personal Training</title>
<link rel="stylesheet" href="https://fonts.googleapis.com/css2?family=Raleway:wght@400;500;600;700&family=Open+Sans:wght@400;600&display=swap">
<style>
:root{
  --orange:#f39a1e;
  --orange-soft:#f7b45a;
  --ink:#2f2f2f;
  --text:#555;
  --muted:#8a8a8a;
  --cream:#f8f6f2;
  --grey:#eeeeee;
  --field:#d6d6d6;
  --dark:#1c1c1c;
  --white:#fff;
}
*{box-sizing:border-box;margin:0;padding:0}
html,body{width:1200px;height:4557px;overflow:hidden}
body{font-family:"Open Sans",Arial,sans-serif;color:var(--text);background:var(--white);position:relative}
.section{position:absolute;left:0;width:1200px}
.abs{position:absolute}
.photo{position:absolute}
h1,h2,h3,h4{font-family:"Raleway",Arial,sans-serif;color:var(--ink)}

/* header */
.site-header{top:0;height:90px;z-index:3}
.brand{left:92px;top:28px;display:flex;align-items:center;gap:10px}
.brand-mark{width:22px;height:22px;background:var(--orange)}
.brand-name{font-family:"Raleway",sans-serif;font-weight:600;font-size:20px;color:var(--orange)}
.main-nav{right:85px;top:34px;display:flex;gap:34px;font-family:"Raleway",sans-serif;font-size:15px;font-weight:500}
.main-nav a{color:var(--ink);text-decoration:none}
.main-nav a.active{color:var(--orange)}

/* hero */
.hero{top:0;height:628px;background:linear-gradient(90deg,#fbfaf8 0%,#f4f1ec 55%,#e9e3da 100%)}
.hero-floor{left:0;top:520px;width:1200px;height:108px;background:linear-gradient(180deg,#e8d9c6,#d9b48f)}
.hero-athlete{left:715px;top:70px;width:440px;height:470px;background:linear-gradient(180deg,#f3d3be,#e98f8a 55%,#4a4a4a);border-radius:40% 40% 8px 8px}
.hero-weights{left:250px;top:540px;width:220px;height:70px;background:linear-gradient(90deg,#f06a7a,#e94b5e);border-radius:14px;opacity:.85}
.hero-copy{left:83px;top:278px;width:560px}
.eyebrow{font-family:"Raleway",sans-serif;font-size:15px;color:var(--ink)}
.hero-copy h1{font-size:34px;font-weight:600;margin:22px 0 18px;color:#3a3a3a}
.hero-copy p{font-size:14px;line-height:1.6;color:var(--orange)}
.btn-outline{display:inline-block;border:1.5px solid var(--orange);border-radius:20px;padding:8px 24px;font-family:"Raleway",sans-serif;font-size:12px;font-weight:600;color:var(--ink);letter-spacing:.5px}
.hero-copy .btn-outline{margin-top:26px}

/* section heading */
.section-title{text-align:center;font-size:30px;font-weight:700}
.divider{position:relative;width:120px;height:14px;margin:12px auto 0}
.divider:before{content:"";position:absolute;left:0;right:0;top:6px;height:1px;background:var(--orange)}
.divider:after{content:"";position:absolute;left:54px;top:1px;width:12px;height:12px;border-radius:50%;background:var(--white);border:2px solid var(--orange);box-sizing:border-box}
.cream .divider:after{background:var(--cream)}
.section-lead{width:700px;margin:18px auto 0;text-align:center;font-size:13px;line-height:1.6;color:var(--muted)}

/* about */
.about{top:628px;height:607px}
.about-copy{left:80px;top:68px;width:560px}
.about-copy h2{font-size:28px;font-weight:700}
.about-copy .divider{margin:12px 0 0 0}
.about-copy p{font-size:13.5px;line-height:1.6;margin-top:20px;color:#444}
.about-copy .btn-outline{margin-top:56px}
.about-frame{left:785px;top:75px;width:336px;height:418px;border:6px solid var(--orange)}
.about-photo{left:743px;top:125px;width:325px;height:413px;background:linear-gradient(180deg,#b7b1a4,#8e8475 55%,#6a6459)}

/* services */
.services{top:1235px;height:610px;background:var(--cream)}
.services .section-title{margin-top:60px}
.card{position:absolute;background:var(--white);box-shadow:0 2px 10px rgba(0,0,0,.06)}
.card-photo{width:100%;height:187px}
.service-card{top:205px;width:332px;height:340px}
.service-card h3{display:flex;align-items:center;gap:10px;font-size:17px;font-weight:700;margin:20px 0 0 20px}
.service-card p{margin:14px 20px 0;font-size:13.5px;line-height:1.6;color:#666}
.slider-arrow{top:330px;width:24px;height:40px}

/* gallery */
.gallery{top:1845px;height:780px}
.gallery .section-title{margin-top:60px}
.tile{position:absolute;width:318px;height:232px}

/* events */
.events{top:2625px;height:610px;background:var(--cream);overflow:hidden}
.events .section-title{margin-top:60px}
.event-waist{left:880px;top:0;width:320px;height:610px;background:linear-gradient(90deg,#c98a66,#a8653f 60%,#6f3f2a)}
.event-back{left:262px;top:230px;width:640px;height:200px;background:var(--white);border:1px solid #ddd}
.event-card{left:285px;top:212px;width:620px;height:222px;background:var(--white);border:1px solid #ddd;box-shadow:0 3px 14px rgba(0,0,0,.12);text-align:center}
.event-card h4{font-size:17px;font-weight:600;margin-top:36px}
.event-card p{font-size:11.5px;line-height:1.6;color:var(--muted);width:420px;margin:14px auto 0}
.event-date{font-size:15px;color:var(--orange);margin-top:14px}
.event-time{font-size:13px;color:#444;margin-top:12px}

/* blog */
.blog{top:3235px;height:680px}
.blog .section-title{margin-top:60px}
.post{top:185px;width:332px;height:415px}
.post .card-photo{height:205px}
.post h3{font-size:15px;font-weight:600;margin:26px 22px 0}
.post .meta{font-size:9.5px;color:var(--muted);margin:12px 22px 0;letter-spacing:.3px;text-transform:uppercase}
.post p{font-size:11.5px;line-height:1.6;color:#666;margin:14px 22px 0}
.post .more{font-size:11.5px;font-weight:600;color:var(--ink);margin:14px 22px 0}

/* contact */
.contact{top:3915px;height:603px;background:var(--grey);overflow:hidden}
.contact .section-title{margin-top:60px;position:relative}
.contact .divider:after{background:var(--grey)}
.contact-model{left:822px;top:0;width:300px;height:603px;background:linear-gradient(180deg,#c7805d,#e2572f 45%,#b2452c 60%,#3b3b3b)}
.contact-list{left:107px;top:235px}
.contact-item{display:flex;align-items:center;gap:22px;height:60px;margin-bottom:42px;font-size:14px;font-weight:600;color:var(--ink);line-height:1.6}
.contact-icon{width:50px;height:50px;border-radius:50%;background:var(--orange);display:flex;align-items:center;justify-content:center;flex:none}
.field{position:absolute;background:var(--field);font-size:12px;color:#555;padding:10px 14px}
.send{position:absolute;left:500px;top:512px;width:170px;height:36px;background:var(--orange);color:var(--white);font-family:"Raleway",sans-serif;font-size:12px;font-weight:600;display:flex;align-items:center;justify-content:center;gap:10px}

/* footer */
.site-footer{top:4518px;height:39px;background:var(--dark);color:#ddd;font-size:12.5px}
.site-footer .copy{left:70px;top:11px}
.social{right:60px;top:15px;display:flex;gap:8px}
.social span{width:9px;height:9px;background:#cfcfcf}
</style>
</head>
<body>

<section class="section hero" id="home">
  <div class="photo hero-floor" role="img" aria-label="Wooden studio floor"></div>
  <div class="photo hero-athlete" role="img" aria-label="Smiling trainer sitting cross-legged in a pink top"></div>
  <div class="photo hero-weights" role="img" aria-label="Pair of pink dumbbells on an exercise mat"></div>
  <div class="abs hero-copy">
    <div class="eyebrow">Welcome Our Website</div>
    <h1>Keep Refresh &amp; Strong Your Body</h1>
    <p>Lorem ipsum dolor sit amet, consectetur adipiscing elit. Integer auctor pharetra leo neque. Nullam cursus elit sit amet justo interdum facilisis id at tortor.</p>
    <span class="btn-outline">READ MORE</span>
  </div>
</section>

<header class="section site-header">
  <div class="abs brand"><span class="brand-mark"></span><span class="brand-name">Marisa Holt</span></div>
  <nav class="abs main-nav">
    <a class="active" href="#home">Home</a>
    <a href="#about">About Me</a>
    <a href="#services">My Services</a>
    <a href="#events">Events</a>
    <a href="#gallery">Gallery</a>
    <a href="#contact">Contact</a>
  </nav>
</header>

<section class="section about" id="about">
  <div class="abs about-copy">
    <h2>About Marisa Holt</h2>
    <div class="divider"></div>
    <p>Lorem Ipsum is simply dummy text of the printing and typesetting industry. Lorem Ipsum has been the industry's standard dummy text ever since the 1500s, when an unknown printer took a galley of type and scrambled it to make a type specimen book. It has survived not only five centuries. Lorem Ipsum is.</p>
    <p>but also the leap into electronic typesetting, remaining essentially unchanged. It was popularised in the 1960s with the release of Letraset sheets containing Lorem Ipsum passages, and more recently with desktop publishing software like Aldus PageMaker including versions.</p>
    <span class="btn-outline">READ MORE</span>
  </div>
  <div class="abs about-frame"></div>
  <div class="photo about-photo" role="img" aria-label="Trainer standing on a beach at the shoreline"></div>
</section>

<section class="section services cream" id="services">
  <h2 class="section-title">Our Services</h2>
  <div class="divider"></div>
  <p class="section-lead">Lorem Ipsum is simply dummy text of the printing and typesetting industry. Lorem Ipsum has been the industry's standard dummy text ever since the 1500s, when an unknown printer</p>

  <svg class="abs slider-arrow" style="left:35px" viewBox="0 0 24 40"><polyline points="18,4 6,20 18,36" fill="none" stroke="#444" stroke-width="2.5"/></svg>
  <svg class="abs slider-arrow" style="left:1142px" viewBox="0 0 24 40"><polyline points="6,4 18,20 6,36" fill="none" stroke="#444" stroke-width="2.5"/></svg>

  <article class="card service-card" style="left:85px">
    <div class="card-photo" role="img" aria-label="Group doing lunges in a gym class" style="background:linear-gradient(135deg,#c9d6e3,#5d7fa6 60%,#2f3e55)"></div>
    <h3><svg width="22" height="14" viewBox="0 0 22 14"><circle cx="6" cy="7" r="5" fill="none" stroke="#f39a1e" stroke-width="2"/><circle cx="16" cy="7" r="5" fill="none" stroke="#f39a1e" stroke-width="2"/></svg>Personal Fitness</h3>
    <p>Lorem Ipsum is simply dummy text of the printing and typesetting industry. Lorem Ipsum has been the industry's type specimen book.</p>
  </article>
  <article class="card service-card" style="left:434px">
    <div class="card-photo" role="img" aria-label="Women exercising together in a studio" style="background:linear-gradient(135deg,#e9b7c9,#b56db0 55%,#5b4a78)"></div>
    <h3><svg width="20" height="18" viewBox="0 0 20 18"><path d="M2 14 L8 4 L12 10 L18 2" fill="none" stroke="#f39a1e" stroke-width="2"/></svg>Physical Activity</h3>
    <p>Lorem Ipsum is simply dummy text of the printing and typesetting industry. Lorem Ipsum has been the industry's type specimen book.</p>
  </article>
  <article class="card service-card" style="left:783px">
    <div class="card-photo" role="img" aria-label="Coach with a clipboard guiding a client" style="background:linear-gradient(135deg,#eef1f4,#a9b9c7 55%,#6c7b88)"></div>
    <h3><svg width="20" height="18" viewBox="0 0 20 18"><path d="M10 16 C2 10 1 6 3 3 C5 1 8 2 10 5 C12 2 15 1 17 3 C19 6 18 10 10 16Z" fill="none" stroke="#f39a1e" stroke-width="2"/></svg>Support &amp; Motivation</h3>
    <p>Lorem Ipsum is simply dummy text of the printing and typesetting industry. Lorem Ipsum has been the industry's type specimen book.</p>
  </article>
</section>

<section class="section gallery" id="gallery">
  <h2 class="section-title">Our Gallery</h2>
  <div class="divider"></div>
  <p class="section-lead">Lorem Ipsum is simply dummy text of the printing and typesetting industry. Lorem Ipsum has been the industry's standard dummy text ever since the 1500s, when an unknown printer</p>
  <div class="photo tile" style="left:98px;top:203px;background:linear-gradient(135deg,#8c8c8c,#3c3c3c)" role="img" aria-label="Man doing chest presses on a gym bench"></div>
  <div class="photo tile" style="left:441px;top:203px;background:linear-gradient(135deg,#d8d8d8,#9a9a9a 50%,#c2362f)" role="img" aria-label="Man in red vest lifting a barbell"></div>
  <div class="photo tile" style="left:784px;top:203px;background:linear-gradient(135deg,#f2f2f2,#8fa7c2 60%,#4f6b8c)" role="img" aria-label="Fitness class stretching together"></div>
  <div class="photo tile" style="left:98px;top:460px;background:linear-gradient(135deg,#6f7f8f,#34414f)" role="img" aria-label="Trainer spotting a woman on a machine"></div>
  <div class="photo tile" style="left:441px;top:460px;background:linear-gradient(180deg,#7fb1dc,#c4d7e6 50%,#c9b08a)" role="img" aria-label="Runner sprinting across a sandy beach"></div>
  <div class="photo tile" style="left:784px;top:460px;background:linear-gradient(135deg,#4c5660,#1f262c)" role="img" aria-label="Athlete flipping a tyre outdoors"></div>
</section>

<section class="section events cream" id="events">
  <div class="photo event-waist" role="img" aria-label="Toned waist wrapped in a yellow measuring tape"></div>
  <h2 class="section-title" style="position:relative">Awesome Event</h2>
  <div class="divider"></div>
  <p class="section-lead" style="position:relative">Lorem Ipsum is simply dummy text of the printing and typesetting industry. Lorem Ipsum has been the industry's standard dummy text ever since the 1500s, when an unknown printer</p>
  <div class="abs event-back"></div>
  <div class="abs event-card">
    <h4>National Conference on Management</h4>
    <p>But I must explain to you how all this mistaken idea of denouncing pleasure and praising pain was born and I will give you a</p>
    <div class="event-date">27 Jul 2017</div>
    <div class="event-time">12:50 AM</div>
    <svg class="abs" style="left:55px;top:94px" width="14" height="22" viewBox="0 0 14 22"><polyline points="11,3 3,11 11,19" fill="none" stroke="#888" stroke-width="2"/></svg>
    <svg class="abs" style="left:550px;top:94px" width="14" height="22" viewBox="0 0 14 22"><polyline points="3,3 11,11 3,19" fill="none" stroke="#888" stroke-width="2"/></svg>
  </div>
</section>

<section class="section blog" id="blog">
  <h2 class="section-title">Our Blog</h2>
  <div class="divider"></div>
  <p class="section-lead">Lorem Ipsum is simply dummy text of the printing and typesetting industry. Lorem Ipsum has been the industry's standard dummy text ever since the 1500s, when an unknown printer</p>
  <article class="card post" style="left:85px">
    <div class="card-photo" role="img" aria-label="Yoga class seated in meditation" style="background:linear-gradient(180deg,#f0ece4,#d9cdb9 60%,#b3a58c)"></div>
    <h3>The Students Learn Different Skills</h3>
    <div class="meta">By Admin · 27 Aug 17 · No Comments</div>
    <p>Lorem ipsum dolor sit amet, consectetur adipiscing elit. Nullam at nibh non justo aliquam euismod ut ac orci. The students learn differ.</p>
    <div class="more">Read More</div>
  </article>
  <article class="card post" style="left:434px">
    <div class="card-photo" role="img" aria-label="Group holding a standing yoga pose" style="background:linear-gradient(180deg,#ece8e2,#c8bfb2 60%,#8d8378)"></div>
    <h3>Best Suitable For Beginners To</h3>
    <div class="meta">By Admin · 27 Aug 17 · No Comments</div>
    <p>Lorem ipsum dolor sit amet, consectetur adipiscing elit. Nullam at nibh non justo aliquam euismod ut ac orci. The students learn differ.</p>
    <div class="more">Read More</div>
  </article>
  <article class="card post" style="left:783px">
    <div class="card-photo" role="img" aria-label="Woman stretching outdoors on grass" style="background:linear-gradient(180deg,#9fcbe8,#8fbf6a 60%,#4f8a3a)"></div>
    <h3>Best Suitable For Beginners To</h3>
    <div class="meta">By Admin · 27 Aug 17 · No Comments</div>
    <p>Lorem ipsum dolor sit amet, consectetur adipiscing elit. Nullam at nibh non justo aliquam euismod ut ac orci. The students learn differ.</p>
    <div class="more">Read More</div>
  </article>
</section>

<section class="section contact" id="contact">
  <div class="photo contact-model" role="img" aria-label="Athlete in an orange sports top"></div>
  <h2 class="section-title">Contact Us</h2>
  <div class="divider"></div>
  <p class="section-lead" style="position:relative">Lorem Ipsum is simply dummy text of the printing and typesetting industry. Lorem Ipsum has been the industry's standard dummy text ever since the 1500s, when an unknown printer</p>

  <div class="abs contact-list">
    <div class="contact-item">
      <span class="contact-icon"><svg width="22" height="22" viewBox="0 0 24 24"><path d="M6.6 10.8a15 15 0 0 0 6.6 6.6l2.2-2.2c.3-.3.7-.4 1-.2 1.1.4 2.3.6 3.6.6.6 0 1 .4 1 1V20c0 .6-.4 1-1 1A17 17 0 0 1 3 4c0-.6.4-1 1-1h3.5c.6 0 1 .4 1 1 0 1.3.2 2.5.6 3.6.1.3 0 .7-.2 1z" fill="#fff"/></svg></span>
      <span>+44 20 7946 0312<br>+44 20 7946 0312</span>
    </div>
    <div class="contact-item">
      <span class="contact-icon"><svg width="22" height="18" viewBox="0 0 22 18"><rect x="1" y="1" width="20" height="16" rx="2" fill="none" stroke="#fff" stroke-width="2"/><polyline points="2,3 11,10 20,3" fill="none" stroke="#fff" stroke-width="2"/></svg></span>
      <span>info@marisaholt.com<br>support@marisaholt.com</span>
    </div>
    <div class="contact-item">
      <span class="contact-icon"><svg width="18" height="24" viewBox="0 0 18 24"><path d="M9 1a8 8 0 0 0-8 8c0 6 8 14 8 14s8-8 8-14a8 8 0 0 0-8-8z" fill="#fff"/><circle cx="9" cy="9" r="3" fill="#f39a1e"/></svg></span>
      <span>48 Fennel Street<br>10422, United States</span>
    </div>
  </div>

  <div class="field" style="left:500px;top:235px;width:275px;height:38px">Name*</div>
  <div class="field" style="left:790px;top:235px;width:255px;height:38px">Email*</div>
  <div class="field" style="left:500px;top:290px;width:545px;height:38px">Subject*</div>
  <div class="field" style="left:500px;top:345px;width:545px;height:152px">Message*</div>
  <div class="send">SEND MESSAGE <svg width="14" height="14" viewBox="0 0 14 14"><polyline points="2,7 6,11 12,3" fill="none" stroke="#fff" stroke-width="2"/></svg></div>
</section>

<footer class="section site-footer">
  <div class="abs copy">©2017 marisaholt. All rights reserved.</div>
  <div class="abs social"><span></span><span></span><span></span><span></span><span></span><span></span><span></span></div>
</footer>

</body>
</html>
```